SkyvoraQ Business Cards and Stationary Design

Need a design for our business cards and stationary. I want to carry on the theme of the logo. I want the business cards to have a design on the back. I would like the business cards and the stationary to carry the same theme, design scheme, and branding

Target Market(s)

Airlines and Maintenance Facilities

Industry/Entity Type

Aviation

Contact Information for Business Card

Name
Position Title
Address: 4827 Tollbeck Lane, Brennock Falls, Vermont, 05871
Office Number
Mobile Number
Email
Website

Font styles to use
Serif
Sans Serif

Colors

Designer to choose colors to be used in the design.

```html
<!DOCTYPE html>
<html lang="en">
<head>
<meta charset="utf-8">
<title>SkyvoraQ Stationery</title>
<link rel="stylesheet" href="https://fonts.googleapis.com/css2?family=Roboto:wght@400;500;700;900&display=swap">
<style>
  :root {
    --backdrop: #3a3a3c;
    --paper: #ffffff;
    --brand-blue: #2490d3;
    --brand-navy: #1b2a55;
    --deep-blue: #1f3a78;
    --mid-blue: #1a7ac0;
    --ink: #1e1e1e;
    --watermark: #e9ebf4;
  }
  * { margin: 0; padding: 0; box-sizing: border-box; }
  html, body { width: 1200px; height: 1034px; overflow: hidden; background: var(--backdrop); }
  body { font-family: "Roboto", Arial, sans-serif; color: var(--ink); }
  .stage { position: relative; width: 1200px; height: 1034px; }

  /* Letterhead */
  .letterhead { position: absolute; left: 54px; top: 58px; width: 650px; height: 920px; background: var(--paper); overflow: hidden; }
  .letterhead .brand { position: absolute; left: 46px; top: 28px; display: flex; align-items: center; gap: 18px; }
  .brand-dot { width: 64px; height: 64px; border-radius: 50%; border: 5px solid var(--brand-navy); }
  .brand-name { font-weight: 700; color: var(--brand-navy); letter-spacing: 5px; font-size: 26px; }
  .letterhead .name-tab { position: absolute; left: 376px; top: 24px; width: 274px; height: 70px; background: var(--brand-blue); border-radius: 35px 0 0 35px; padding: 9px 0 0 42px; color: #fff; }
  .name-tab .person { font-size: 24px; font-weight: 900; line-height: 1.15; }
  .name-tab .role { font-size: 17px; font-weight: 500; margin-top: 2px; }
  .letterhead .watermark { position: absolute; left: 124px; top: 226px; width: 464px; height: 464px; border-radius: 50%; border: 30px solid var(--watermark); }
  .contact-row { position: absolute; left: 0; top: 820px; width: 650px; height: 60px; }
  .contact-item { position: absolute; top: 0; width: 160px; margin-left: -80px; text-align: center; font-size: 10px; font-weight: 500; }
  .contact-item svg { display: block; margin: 0 auto 10px; width: 24px; height: 24px; }
  .letterhead .address-band { position: absolute; left: 0; bottom: 0; width: 650px; height: 37px; background: var(--brand-blue); color: #fff; font-size: 11.5px; font-weight: 500; display: flex; align-items: center; justify-content: center; gap: 10px; }

  /* Card front */
  .card { position: absolute; left: 740px; width: 402px; box-shadow: 6px 6px 8px rgba(0,0,0,.45); overflow: hidden; }
  .card-front { top: 62px; height: 229px; background: linear-gradient(90deg, var(--mid-blue), var(--deep-blue)); }
  .card-front .brand-dot { position: absolute; left: 150px; top: 46px; width: 88px; height: 88px; border: 6px solid var(--brand-navy); }
  .card-front .brand-name { position: absolute; left: 0; top: 146px; width: 100%; text-align: center; font-size: 30px; letter-spacing: 7px; }

  /* Card back */
  .card-back { top: 310px; height: 230px; background: var(--paper); }
  .card-back .watermark { position: absolute; left: 206px; top: 28px; width: 168px; height: 168px; border-radius: 50%; border: 12px solid var(--watermark); }
  .card-back .brand-dot { position: absolute; left: 276px; top: 28px; width: 38px; height: 38px; border: 3px solid var(--brand-navy); }
  .card-back .brand-name { position: absolute; left: 230px; top: 69px; width: 130px; text-align: center; font-size: 14px; letter-spacing: 2.5px; }
  .card-back .person { position: absolute; left: 37px; top: 35px; font-size: 14.5px; font-weight: 900; color: var(--brand-blue); }
  .card-back .role { position: absolute; left: 37px; top: 55px; font-size: 11px; font-weight: 500; }
  .card-contacts { position: absolute; left: 0; top: 104px; list-style: none; }
  .card-contacts li { display: flex; align-items: center; height: 20px; font-size: 11px; font-weight: 500; }
  .card-contacts .tab { width: 24px; height: 16px; background: var(--brand-blue); border-radius: 0 6px 6px 0; margin-right: 13px; display: flex; align-items: center; justify-content: center; }
  .card-contacts .tab svg { width: 10px; height: 10px; }
  .card-back .base-band { position: absolute; left: 0; bottom: 0; width: 100%; height: 8px; background: var(--brand-blue); }
</style>
</head>
<body>
<div class="stage">

  <section class="letterhead">
    <div class="brand"><span class="brand-dot"></span><span class="brand-name">SKYVORAQ</span></div>
    <div class="name-tab">
      <div class="person">Your Name Here</div>
      <div class="role">Position Title</div>
    </div>
    <div class="watermark"></div>

    <div class="contact-row">
      <div class="contact-item" style="left:88px">
        <svg viewBox="0 0 24 24" fill="#2490d3"><path d="M6.6 10.8a15.1 15.1 0 0 0 6.6 6.6l2.2-2.2c.3-.3.7-.4 1-.2 1.1.4 2.3.6 3.6.6.6 0 1 .4 1 1V20c0 .6-.4 1-1 1A17 17 0 0 1 3 4c0-.6.4-1 1-1h3.5c.6 0 1 .4 1 1 0 1.3.2 2.5.6 3.6.1.3 0 .7-.2 1z"/></svg>
        Your office no. here
      </div>
      <div class="contact-item" style="left:224px">
        <svg viewBox="0 0 24 24" fill="none" stroke="#2490d3" stroke-width="2"><rect x="7" y="2" width="10" height="20" rx="1.5"/><line x1="11" y1="19" x2="13" y2="19"/></svg>
        Your mobile no. here
      </div>
      <div class="contact-item" style="left:382px">
        <svg viewBox="0 0 24 24" fill="none" stroke="#2490d3" stroke-width="1.8"><rect x="2" y="5" width="20" height="14"/><path d="M2 5l10 8 10-8M2 19l7-7M22 19l-7-7"/></svg>
        youremailid@skyvoraq.com
      </div>
      <div class="contact-item" style="left:548px">
        <svg viewBox="0 0 24 24" fill="none" stroke="#2490d3" stroke-width="1.6"><circle cx="12" cy="12" r="10"/><ellipse cx="12" cy="12" rx="4.5" ry="10"/><path d="M2 12h20M4 7h16M4 17h16"/></svg>
        www.yourwebaddress.com
      </div>
    </div>

    <div class="address-band">
      <svg width="14" height="14" viewBox="0 0 24 24" fill="none" stroke="#fff" stroke-width="2"><path d="M12 22s-7-7-7-12a7 7 0 0 1 14 0c0 5-7 12-7 12z"/><circle cx="12" cy="10" r="2.5"/></svg>
      Address: 4827 Tollbeck Lane, Brennock Falls, Vermont, 05871
    </div>
  </section>

  <section class="card card-front">
    <span class="brand-dot"></span>
    <span class="brand-name">SKYVORAQ</span>
  </section>

  <section class="card card-back">
    <div class="watermark"></div>
    <span class="brand-dot"></span>
    <span class="brand-name">SKYVORAQ</span>
    <div class="person">Your Name Here</div>
    <div class="role">Position Title</div>
    <ul class="card-contacts">
      <li><span class="tab"><svg viewBox="0 0 24 24" fill="#fff"><path d="M6.6 10.8a15.1 15.1 0 0 0 6.6 6.6l2.2-2.2c.3-.3.7-.4 1-.2 1.1.4 2.3.6 3.6.6.6 0 1 .4 1 1V20c0 .6-.4 1-1 1A17 17 0 0 1 3 4c0-.6.4-1 1-1h3.5c.6 0 1 .4 1 1 0 1.3.2 2.5.6 3.6.1.3 0 .7-.2 1z"/></svg></span>Your office no. here</li>
      <li><span class="tab"><svg viewBox="0 0 24 24" fill="none" stroke="#fff" stroke-width="2.5"><rect x="7" y="2" width="10" height="20" rx="1.5"/></svg></span>Your mobile no. here</li>
      <li><span class="tab"><svg viewBox="0 0 24 24" fill="none" stroke="#fff" stroke-width="2.2"><rect x="2" y="5" width="20" height="14"/><path d="M2 5l10 8 10-8"/></svg></span>youremailid@skyvoraq.com</li>
      <li><span class="tab"><svg viewBox="0 0 24 24" fill="none" stroke="#fff" stroke-width="2"><circle cx="12" cy="12" r="10"/><ellipse cx="12" cy="12" rx="4.5" ry="10"/><path d="M2 12h20"/></svg></span>www.yourwebaddress.com</li>
      <li><span class="tab"><svg viewBox="0 0 24 24" fill="none" stroke="#fff" stroke-width="2.4"><path d="M12 22s-7-7-7-12a7 7 0 0 1 14 0c0 5-7 12-7 12z"/><circle cx="12" cy="10" r="2.5"/></svg></span>Address: 4827 Tollbeck Lane, Brennock Falls, Vermont, 05871</li>
    </ul>
    <div class="base-band"></div>
  </section>

</div>
</body>
</html>
```